Tampa Bay fishing guide needs stunning website.

I currently have a site - www.reelcoastcharters.example which I personally put together using the Plimo platform and I am looking for a redesign on a different platform (Sitebarn?) that will allow me to easily create landing pages in the future. Would like to have a block for visitors to opt in to newsletter. Need social media links on all pages.

I would like to let my visitors know that I am able to handle their fishing charter needs here in the Tampa Bay area, if I'm not available for the dates they are looking to go I can refer them to a reputable captain in the area.

Target Market(s)

United States

Industry/Entity Type

Tourism

Coding

Coded - Design and coding required

Number of Pages Required

5+ page

Font styles to use
Sans Serif

Colors
0355a3
3176b5
85abd2
fbf289

Requirements
Must have
• Mobile Responsive, Ability to insert Trackwise Metrics, Chatterly pixels, ability to add custom landing pages in future
Nice to have
• Clean, easy navigation

```html
<!DOCTYPE html>
<html lang="en">
<head>
<meta charset="utf-8">
<title>Capt. Dale Harrow – Tampa Bay Fishing Charters</title>
<link rel="stylesheet" href="https://fonts.googleapis.com/css2?family=Catamaran:wght@300;400;600;700;800&family=Open+Sans:wght@400;600;700&display=swap">
<style>
:root{
  --blue:#0355a3;
  --blue-mid:#3176b5;
  --blue-light:#85abd2;
  --yellow:#fbf289;
  --yellow-strong:#f7ea3a;
  --gold:#f0d82a;
  --navy:#0a2a5c;
  --dark:#141a22;
  --ink:#111;
  --white:#fff;
}
*{margin:0;padding:0;box-sizing:border-box}
html,body{width:1200px;height:3383px;overflow:hidden}
body{position:relative;font-family:"Open Sans",Arial,sans-serif;color:var(--ink);background:var(--white)}
a{text-decoration:none}
.abs{position:absolute}
h1,h2,h3{font-family:"Catamaran",Arial,sans-serif;line-height:1.1}
.btn{position:absolute;display:flex;align-items:center;justify-content:center;font-family:"Open Sans",Arial,sans-serif;font-weight:700;font-size:18px;border-radius:2px;text-decoration:none}
.btn-blue{background:var(--blue);color:var(--white)}
.btn-yellow{background:var(--yellow-strong);color:var(--ink)}
.rule{position:absolute;height:4px;width:68px}

/* header */
.site-header{top:0;left:0;width:1200px;height:124px;background:var(--white)}
.brand{left:56px;top:36px;display:flex;align-items:center;gap:12px}
.brand-dot{width:40px;height:40px;border-radius:50%;background:var(--blue-mid)}
.brand-name{font-family:"Catamaran",sans-serif;font-weight:700;font-size:30px;color:var(--blue);line-height:1}
.call{left:946px;top:14px;display:flex;align-items:center;gap:10px}
.call-text{font-size:14px;line-height:17px;color:#333}
.call-text b{display:block;color:var(--blue);font-size:16px;font-weight:600}
.nav{left:471px;top:74px;display:flex;font-family:"Catamaran",sans-serif;font-weight:700;font-size:16px}
.nav a{display:block;padding:7px 10px;color:var(--ink);line-height:20px}
.nav a.active{background:var(--blue);color:var(--white)}

/* hero */
.hero{top:124px;left:0;width:1200px;height:576px;background:var(--yellow)}
.hero-photo{top:0;left:0;width:1200px;height:576px;background:linear-gradient(135deg,#8fb6cc 0%,#cfd8dc 40%,#6c8fa6 70%,#375e7c 100%);clip-path:polygon(812px 0,1200px 0,1200px 576px,451px 576px)}
.hero h1{left:61px;top:100px;font-size:42px;line-height:62px;font-weight:800;color:var(--ink);letter-spacing:.5px;white-space:nowrap}
.hero p{left:61px;top:300px;width:440px;font-size:13px;line-height:20px}
.hero .btn{left:61px;top:408px;width:153px;height:43px}

/* who */
.who{top:700px;left:0;width:1200px;height:320px;background:var(--blue);color:var(--white);text-align:center}
.who h2{position:absolute;left:0;width:1200px;top:44px;font-weight:400;font-size:44px}
.who .rule{left:566px;top:104px;background:var(--white)}
.who p{left:135px;top:146px;width:930px;font-size:13px;line-height:24px}
.who .btn{left:523px;top:234px;width:147px;height:43px}

/* what we do */
.what{top:1020px;left:0;width:1200px;height:965px;background:linear-gradient(180deg,#2a3038 0%,#1a2029 45%,#3a4148 100%)}
.what h2{position:absolute;left:0;width:1200px;top:60px;text-align:center;color:var(--white);font-weight:400;font-size:44px}
.what .rule{left:566px;top:120px;background:var(--gold)}
.service{position:absolute;top:187px;width:360px;text-align:center;color:var(--white)}
.service .icon{width:140px;height:140px;margin:0 auto;border-radius:50%;background:var(--white);border:4px solid var(--gold);display:flex;align-items:center;justify-content:center}
.service h3{margin-top:28px;color:var(--gold);font-weight:600;font-size:22px;text-transform:uppercase}
.service p{font-size:13px;line-height:20px;margin-top:4px}

/* captain */
.captain-band{top:1490px;left:0;width:620px;height:495px;background:var(--yellow);clip-path:polygon(0 0,620px 90px,620px 495px,0 495px)}
.captain-photo{top:1490px;left:620px;width:580px;height:495px;background:linear-gradient(160deg,#3a6f8e 0%,#6f95ab 45%,#d9dde0 80%,#b8c2c9 100%)}
.captain h2{left:61px;top:1636px;font-weight:400;font-size:38px;color:var(--blue)}
.captain .rule{left:61px;top:1684px;background:var(--blue)}
.captain p{left:61px;width:520px;font-size:13px;line-height:21px}
.captain .btn{left:61px;top:1888px;width:253px;height:43px;font-size:16px}

/* help */
.help-photo{top:1985px;left:0;width:620px;height:391px;background:linear-gradient(150deg,#4f6f85 0%,#8aa7b8 40%,#c9d3da 60%,#2c3f50 100%)}
.help-band{top:1985px;left:620px;width:580px;height:391px;background:var(--yellow)}
.help h2{left:650px;top:2060px;font-weight:400;font-size:38px;color:var(--blue)}
.help .rule{left:650px;top:2109px;background:var(--blue)}
.help p{left:654px;top:2136px;width:510px;font-size:13px;line-height:20px}
.help .btn{left:654px;top:2290px;width:199px;height:43px;font-size:16px}

/* testimonials */
.say{top:2376px;left:0;width:1200px;height:430px;background:linear-gradient(180deg,#06306d 0%,#0a3f86 55%,#1f5db0 100%)}
.say h2{position:absolute;left:0;width:1200px;top:60px;text-align:center;color:var(--white);font-weight:400;font-size:40px}
.say .rule{left:566px;top:124px;background:var(--gold)}
.quote{position:absolute;top:175px;display:flex;gap:16px;width:330px}
.quote .avatar{flex:none;width:86px;height:86px;border-radius:50%;background:linear-gradient(180deg,#d8b48a,#b58a5c);border:4px solid var(--gold)}
.quote blockquote{color:var(--white);font-size:14px;line-height:19px;padding-top:14px;width:210px}
.quote blockquote .mark{font-family:"Catamaran",sans-serif;font-size:28px;line-height:10px;vertical-align:-8px;margin-right:4px}
.quote cite{display:block;font-style:normal;color:var(--gold);font-weight:600;font-size:14px;line-height:19px;margin-top:12px}

/* contact */
.contact{top:2740px;left:0;width:1200px;height:595px;background:linear-gradient(180deg,#222a33 0%,#0c0f14 100%);clip-path:polygon(0 40px,600px 0,1200px 40px,1200px 595px,0 595px)}
.contact h2{position:absolute;left:0;width:1200px;top:180px;text-align:center;color:var(--white);font-weight:400;font-size:42px}
.contact .rule{left:566px;top:245px;background:var(--gold)}
.subscribe{left:311px;top:319px;display:flex}
.subscribe .field{width:449px;height:45px;background:var(--white);font-size:14px;color:#777;padding:13px 16px}
.subscribe .btn{position:static;width:133px;height:45px;background:var(--yellow-strong);color:var(--ink);font-size:18px}
.info{color:var(--white);font-size:13px;line-height:20px;font-weight:600}
.info-row{display:flex;gap:12px;align-items:flex-start}
.socials{display:flex;gap:8px}
.socials span{width:26px;height:26px;border-radius:50%;background:var(--blue-mid)}
.pay-name{left:0;width:1200px;top:3240px;text-align:center;color:var(--white);font-family:"Catamaran",sans-serif;font-weight:700;font-size:24px;line-height:1}
.cards{left:487px;top:3284px;display:flex;gap:6px}
.cards span{width:36px;height:22px;background:#e5e5e5;border-radius:2px}
.footer{top:3335px;left:0;width:1200px;height:48px;background:#050607;color:var(--white);font-size:13px;text-align:center;line-height:48px}
</style>
</head>
<body>

<header class="site-header abs">
  <div class="brand abs"><span class="brand-dot"></span><span class="brand-name">Capt. Dale Harrow</span></div>
  <div class="call abs">
    <svg width="26" height="26" viewBox="0 0 24 24"><circle cx="12" cy="12" r="11" fill="none" stroke="#0355a3" stroke-width="1.5"/><path d="M8 6.5l2 .3 1 2.6-1.3 1c.6 1.4 1.6 2.4 3 3l1-1.3 2.6 1 .3 2c-.3.7-1 1.2-1.8 1.2C10.6 16.2 7.8 13.4 7.7 8.3c0-.8.5-1.5 1.3-1.8z" fill="#0355a3"/></svg>
    <div class="call-text">Call Now<b>555-014-2290</b></div>
  </div>
  <nav class="nav abs">
    <a class="active" href="#">HOME</a><a href="#">ABOUT US</a><a href="#">PICK UP</a><a href="#">LOCATIONS</a><a href="#">RATES</a><a href="#">CONTACT US</a><a href="#">GIFT CARD</a>
  </nav>
</header>

<section class="hero abs">
  <div class="hero-photo abs" role="img" aria-label="Anglers on a boat unhooking a large tarpon beside the hull"></div>
  <h1 class="abs">TAMPA BAY, FISHING GUIDE<br>TAMPA BAY FISHING<br>CHARTERS</h1>
  <p class="abs">Capt. Dale Harrow, with over 20 years' experience. Native fishing charter tampa charter captain offering full and half day fishing charters on the waters of Tampa Bay.</p>
  <a class="btn btn-blue" href="#">Know More</a>
</section>

<section class="who abs">
  <h2>WHO WE ARE</h2>
  <span class="rule"></span>
  <p class="abs">Lorem Ipsum is simply dummy text of the printing and typesetting industry. Lorem Ipsum has been the industry's standard dummy text ever since the 1500s, when an unknown printer took a galley of type and scrambled it to make a type specimen book.Lorem Ipsum is simply dummy text of the printing and typesetting industry. Lorem Ipsum has been the industry's standard</p>
  <a class="btn btn-yellow" href="#">Contact us</a>
</section>

<section class="what abs" role="img" aria-label="Dimmed photo of the captain with a guest on the water">
  <h2>WHAT WE DO</h2>
  <span class="rule"></span>
  <div class="service" style="left:59px">
    <div class="icon"><svg width="70" height="70" viewBox="0 0 64 64" fill="none" stroke="#0355a3" stroke-width="5" stroke-linecap="round" stroke-linejoin="round"><path d="M54 30a22 22 0 1 1-8-17"/><path d="M20 31l10 10 26-26"/></svg></div>
    <h3>Full &amp; Half Day Charters</h3>
    <p>Lorem Ipsum is simply dummy text of the printing<br>and typesetting industry...</p>
  </div>
  <div class="service" style="left:420px">
    <div class="icon"><svg width="72" height="72" viewBox="0 0 64 64" fill="none" stroke="#0355a3" stroke-width="3.5" stroke-linejoin="round"><path d="M12 26l20-14 20 14v26H12z"/><rect x="20" y="34" width="16" height="14"/><path d="M20 40h16M28 34v6"/><path d="M40 20a8 8 0 0 1 12 6" stroke-linecap="round"/><path d="M52 20v6h-6" stroke-linecap="round"/></svg></div>
    <h3>Multiple Pickup Points</h3>
    <p>Lorem Ipsum is simply dummy text of the printing<br>and typesetting industry...</p>
  </div>
  <div class="service" style="left:790px">
    <div class="icon"><svg width="72" height="72" viewBox="0 0 64 64" fill="#0355a3"><circle cx="22" cy="18" r="7"/><path d="M10 38c0-8 5-12 12-12s12 4 12 12z"/><circle cx="44" cy="32" r="7"/><path d="M32 52c0-8 5-12 12-12s12 4 12 12z"/><path d="M40 12a12 12 0 0 1 10 10l3-2M24 52a12 12 0 0 1-10-8l-3 2" fill="none" stroke="#0355a3" stroke-width="3" stroke-linecap="round"/></svg></div>
    <h3>Consulation</h3>
    <p>Lorem Ipsum is simply dummy text of the printing<br>and typesetting industry...</p>
  </div>
</section>

<section class="captain">
  <div class="captain-band abs"></div>
  <div class="captain-photo abs" role="img" aria-label="Portrait of the captain in a cap on the water"></div>
  <h2 class="abs">CAPT. DALE HARROW</h2>
  <span class="rule"></span>
  <p class="abs" style="top:1714px">Capt. Dale was born and raised in the Tampa Bay area and fell in love with fishing as a very young boy. He has guided some of the world's top name celebrities and politicians. Through his passion and hard work he has earned a living as a full time guide in the Tampa Bay area for over 25 years.</p>
  <p class="abs" style="top:1820px">Capt. Dale invites you and your guests to come aboard and enjoy the thrills of fishing for the top gamefish that Tampa Bay has to offer.</p>
  <a class="btn btn-blue" href="#">Check the Rate to hire Capt.</a>
</section>

<section class="help">
  <div class="help-photo abs" role="img" aria-label="Captain and guest holding up a tarpon on deck"></div>
  <div class="help-band abs"></div>
  <h2 class="abs">HOW WE CAN HELP</h2>
  <span class="rule"></span>
  <p class="abs">Lorem Ipsum is simply dummy text of the printing and typesetting industry. Lorem Ipsum has been the industry's standard dummy text ever since the 1500s, when an unknown printer took a galley of type and scrambled it to make a type specimen book.Lorem Ipsum is simply dummy text of the printing and typesetting industry. Lorem Ipsum has been the industry's standard dummy text ever since the 1500s.</p>
  <a class="btn btn-blue" href="#">Give the Perfect Gift</a>
</section>

<section class="say abs">
  <h2>WHAT PEOPLE SAY</h2>
  <span class="rule"></span>
  <div class="quote" style="left:66px">
    <div class="avatar" role="img" aria-label="Reviewer portrait"></div>
    <blockquote><span class="mark">&ldquo;</span>Capt. Dale has always been a 100%er for me<cite>Rob Kessler<br>Outdoor Editor for Bayshore Herald</cite></blockquote>
  </div>
  <div class="quote" style="left:440px">
    <div class="avatar" role="img" aria-label="Reviewer portrait"></div>
    <blockquote><span class="mark">&ldquo;</span>Truly a master angler<cite>Lena Ortiz<br>former Harbor County Commissioner</cite></blockquote>
  </div>
  <div class="quote" style="left:794px">
    <div class="avatar" role="img" aria-label="Reviewer portrait"></div>
    <blockquote><span class="mark">&ldquo;</span>Congratulations on winning the Gulf Coast Celebrity Grand Slam Tournament<cite>Marcus Hale<br>Former State Senator</cite></blockquote>
  </div>
</section>

<section class="contact abs" role="img" aria-label="Dark photo of anglers on the bay behind the contact area">
  <h2>CONTACT US</h2>
  <span class="rule"></span>
  <form class="subscribe abs"><div class="field">Your Email</div><span class="btn">Subscribe</span></form>
  <div class="info abs" style="left:306px;top:400px">
    <div class="info-row"><svg width="16" height="20" viewBox="0 0 16 20"><path d="M8 1a6 6 0 0 0-6 6c0 4.5 6 12 6 12s6-7.5 6-12a6 6 0 0 0-6-6z" fill="#f7ea3a"/><circle cx="8" cy="7" r="2.3" fill="#141a22"/></svg>
      <div>Harborview Marina - St. Petersburg<br>Pelican Cove - Ruskin<br>Bayside Boat Ramp<br>Kingston Boat Ramp</div></div>
  </div>
  <div class="info abs" style="left:664px;top:400px">
    <div class="info-row"><svg width="16" height="16" viewBox="0 0 24 24"><path d="M5 3l4 .5 1.6 4.4-2.3 1.7c1 2.3 2.8 4.1 5.1 5.1l1.7-2.3 4.4 1.6.5 4c-.5 1.2-1.6 2-3 2C9.5 19.9 4 14.4 3 6c0-1.4.8-2.6 2-3z" fill="#f7ea3a"/></svg><span>TEL: 555-014-2290</span></div>
    <div class="info-row" style="margin-top:8px"><svg width="16" height="16" viewBox="0 0 24 24"><rect x="2" y="5" width="20" height="14" fill="#f7ea3a"/><path d="M2 5l10 8 10-8" fill="none" stroke="#141a22" stroke-width="2"/></svg><span>E-MAIL: captdale@reelcoast.example</span></div>
    <div class="socials" style="margin-top:10px"><span></span><span></span><span></span><span></span></div>
  </div>
</section>
<div class="pay-name abs">PayLink</div>
<div class="cards abs"><span></span><span></span><span></span><span></span><span></span></div>

<footer class="footer abs">© 2005 - 2016 CAPT. DALE HARROW ALL RIGHT RESERVED</footer>

</body>
</html>
```